R7M Horizon Business Card Design

We need a business card created for our New Business "R7M Horizon"<br/><br/>The business card design is up to you however the following information must be on the business card:<br/><br/>Front of the business card -<br/>Email :tobyw@r7mhorizon.nz<br/>Mobile: +64 (0) 22 4871 569<br/>Website: www.r7mhorizon.nz<br/>Card Owner Name: Tobias Wrenhall<br/>Company Title: Business Development Manager<br/>Slogan: "The BEST of both worlds". <br/>Logo On the front attached to the design brief<br/><br/>On the back: <br/>Space on the back for 4 more versions of the logo across the bottom of the card indicating different subsidiary brands - R7M Coffee, R7M Arts, R7M ?? (The card will be used for all of these brands - We Will add the extra subsidiary logos to the design once the design is finished (We are a graphics design team). <br/><br/>Other than that we want a premium feeling logo that remains universally usable depending on the business entity that we are using the card for. The use of bright bold colours would be great but we still want the card to feel premium.
Target Market(s)
Gift Design and Manufacturing Companies
Contact Information for Business Card
Front of the business card -
Email :tobyw@r7mhorizon.nz
Mobile: +64 (0) 22 4871 569
Website: www.r7mhorizon.nz
Card Owner Name: Tobias Wrenhall
Company Title: Business Development Manager
Slogan: "The BEST of both worlds".
Logo On the front attached to the design brief

```html
<!DOCTYPE html>
<html lang="en">
<head>
<meta charset="utf-8">
<title>R7M Horizon Business Card</title>
<link href="https://fonts.googleapis.com/css2?family=Krona+One&family=Open+Sans:wght@400;600;700&display=swap" rel="stylesheet">
<style>
  :root {
    --page-bg: #e4e4e6;
    --card-dark: #1b1b1b;
    --card-light: #ffffff;
    --brand-blue: #2f3ea3;
    --ink: #2a2a2a;
    --white: #ffffff;
  }
  * { box-sizing: border-box; margin: 0; padding: 0; }
  html, body {
    width: 1200px; height: 900px; overflow: hidden;
    background: var(--page-bg);
    font-family: "Open Sans", Arial, sans-serif;
  }
  .card {
    position: absolute;
    left: 320px;
    width: 560px; height: 320px;
    border-radius: 36px;
    box-shadow: 0 10px 28px rgba(0,0,0,0.22);
  }
  .card--back { top: 90px; background: var(--card-dark); }
  .card--front { top: 490px; background: var(--card-light); }

  .brand {
    font-family: "Open Sans", Arial, sans-serif;
    font-weight: 700;
    white-space: nowrap;
    line-height: 1.2;
  }
  .card--back .brand {
    position: absolute; left: 0; right: 0; top: 104px;
    text-align: center;
    color: var(--white);
    font-size: 44px;
  }
  .slogan {
    position: absolute; left: 0; right: 0; bottom: 42px;
    text-align: center;
    color: var(--white);
    font-size: 15px;
    letter-spacing: 0.3px;
  }
  .slogan strong { font-weight: 700; }
  .slogan__arrow { font-size: 10px; margin: 0 8px; vertical-align: 1px; }

  .card--front .brand {
    position: absolute; right: 40px; top: 62px;
    color: var(--brand-blue);
    font-size: 28px;
  }

  .owner {
    position: absolute; left: 44px; top: 170px;
  }
  .owner__name {
    font-family: "Krona One", Arial, sans-serif;
    font-size: 19px;
    font-weight: 400;
    color: var(--brand-blue);
    text-transform: uppercase;
    letter-spacing: 0.5px;
  }
  .owner__title {
    font-size: 14px; color: var(--ink); margin-top: 2px;
  }
  .contacts {
    list-style: none; margin-top: 14px; margin-left: 20px;
  }
  .contacts li {
    display: flex; align-items: center; gap: 10px;
    font-size: 14px; color: var(--ink); line-height: 22px;
  }
  .contacts svg { width: 12px; height: 12px; fill: var(--brand-blue); flex: none; }
</style>
</head>
<body>
  <section class="card card--back">
    <div class="brand">R7M Horizon</div>
    <p class="slogan"><span class="slogan__arrow">&#9664;</span>The <strong>BEST</strong> of both worlds<span class="slogan__arrow">&#9654;</span></p>
  </section>

  <section class="card card--front">
    <div class="brand">R7M Horizon</div>
    <div class="owner">
      <h1 class="owner__name">Tobias Wrenhall</h1>
      <p class="owner__title">Business Development Manager</p>
      <ul class="contacts">
        <li>
          <svg viewBox="0 0 12 12" aria-hidden="true"><path d="M2.5 0.8l2 2.2-1 1.3c.6 1.4 1.8 2.6 3.2 3.2l1.3-1 2.2 2-1.2 2C5.5 10.4 1.6 6.5 0.5 2z"/></svg>
          +64 (0) 22 4871 569
        </li>
        <li>
          <svg viewBox="0 0 12 12" aria-hidden="true"><path d="M0.5 2h11v8h-11z M1.5 3v.3L6 6.5l4.5-3.2V3z M1.5 4.5V9h9V4.5L6 7.7z" fill-rule="evenodd"/></svg>
          tobyw@r7mhorizon.nz
        </li>
        <li>
          <svg viewBox="0 0 12 12" aria-hidden="true"><circle cx="6" cy="6" r="5.5"/><path d="M0.5 6h11M6 0.5c-2 2.5-2 8.5 0 11M6 0.5c2 2.5 2 8.5 0 11" stroke="#fff" stroke-width="0.8" fill="none"/></svg>
          www.r7mhorizon.nz
        </li>
      </ul>
    </div>
  </section>
</body>
</html>
```